Postcard and Door Hanger Design

We need two pieces designed for marketing. Both will use the same logo and photo just the text will be slightly different. We need these designs looking very modern, clean, and simple while having the important information to stand out.

Postcard: 2 sided
- Side 1 just have large logo with our website and phone number
- Side 2 below.
- 4 x 6
- Use photo of house provided
- "Going Above and Beyond Every Time"
- "Call TODAY to Reserve your project by May 1st and receive 10% off"
- "Residential and Commercial"
- Our contact is 250-555-0147
- Website is www.brightoakcoatings.com
- Might include something like "check out our portfolio on our website"

Use the above as a guidline and be creative with it, add or take away as you see fit as we are open to suggestions.

Door Hanger: 2 sided
Side 1 - Logo with contact details
Side 2 - Below
- 4 x 11
- "We are painting your neighborhood"
-"come see us in action at (then leave a space where we can stick a label onto our door hanger with an address of a home we are painting)
- Call today for a FREE ESTIMATE
- 250-555-0147
- www.brightoakcoatings.com

https://www.filenook.net/sh/42qrt19k3mzp5xa/RT7KLMN-QZ

https://www.filenook.net/sh/tt3ru58w7jxe21c/LMwRRJnoQx

https://www.filenook.net/sh/p3z55rf6wqn44dd/xvt-Hj2KWa

```html
<!DOCTYPE html>
<html lang="en">
<head>
<meta charset="utf-8">
<title>Bright Oak Coatings – Postcard Front</title>
<link rel="stylesheet" href="https://fonts.googleapis.com/css2?family=Cinzel:wght@400&family=Arimo:wght@400;700&display=swap">
<style>
  :root {
    --backdrop: #e9e7e4;
    --slate: #465560;
    --teal: #17bdb8;
    --white: #ffffff;
  }
  html, body {
    margin: 0;
    padding: 0;
    width: 1200px;
    height: 988px;
    overflow: hidden;
    background: var(--backdrop);
  }
  .postcard {
    position: absolute;
    left: 110px;
    top: 117px;
    width: 980px;
    height: 753px;
    background: var(--slate);
    box-shadow: 0 4px 14px rgba(0, 0, 0, 0.25);
  }
  .brand-square {
    position: absolute;
    left: 434px;
    top: 160px;
    width: 112px;
    height: 112px;
    background: var(--teal);
    border-radius: 6px;
  }
  .wordmark {
    position: absolute;
    left: 0;
    width: 100%;
    top: 338px;
    text-align: center;
    color: var(--white);
    font-family: "Cinzel", "Trajan Pro", serif;
    font-weight: 400;
  }
  .wordmark-name {
    display: block;
    font-size: 66px;
    line-height: 1;
    letter-spacing: 3px;
  }
  .wordmark-trade {
    display: block;
    margin-top: 28px;
    font-size: 28px;
    line-height: 1;
    letter-spacing: 34px;
    padding-left: 34px;
  }
  .contact-band {
    position: absolute;
    left: 0;
    top: 578px;
    width: 100%;
    height: 125px;
    background: var(--teal);
    color: var(--white);
    font-family: "Arimo", "Helvetica Neue", Arial, sans-serif;
  }
  .phone {
    position: absolute;
    left: 48px;
    top: 38px;
    display: flex;
    align-items: center;
    gap: 14px;
    font-size: 48px;
    font-weight: 400;
    line-height: 1;
  }
  .phone-icon {
    width: 46px;
    height: 46px;
  }
  .website {
    position: absolute;
    right: 55px;
    top: 50px;
    font-size: 26px;
    font-weight: 700;
    line-height: 1;
  }
</style>
</head>
<body>
  <main class="postcard">
    <div class="brand-square" aria-hidden="true"></div>
    <h1 class="wordmark">
      <span class="wordmark-name">BRIGHT OAK</span>
      <span class="wordmark-trade">COATINGS</span>
    </h1>
    <footer class="contact-band">
      <div class="phone">
        <svg class="phone-icon" viewBox="0 0 46 46" aria-hidden="true">
          <circle cx="23" cy="23" r="21" fill="none" stroke="#ffffff" stroke-width="2.5"/>
          <path d="M17 11 h5 l1 7 -4 2 c1 3 2 6 4 8 l4 -2 5 5 -3 4 c-8 -1 -14 -10 -15 -20 z" fill="#ffffff"/>
        </svg>
        <span>(250) 555-0147</span>
      </div>
      <div class="website">www.brightoakcoatings.com</div>
    </footer>
  </main>
</body>
</html>
```